One page financial canvas needed

I am in the process of developing a financial planning process that uses a one page canvas as a tool for financial education and to explain simple and complex financial strategies to clients. I have the layout and content sorted, just need a hand making it look professional.

It should be a fairly simple project and i have attached a very rough hand drawn canvas showing the desired layout and content. Please feel free to be creative with the design keeping in mind this layout has been chosen to achieve certain outcomes.

Target Market(s)

25-45 Year old Homeowners who are interested in taking better care of the finances

Industry/Entity Type

Financial

Colors

Designer to choose colors to be used in the design.

Requirements
Must have
• very close to the layout in the attached file

```html
<!DOCTYPE html>
<html lang="en">
<head>
<meta charset="utf-8">
<title>Financial Planning Canvas</title>
<link rel="stylesheet" href="https://fonts.googleapis.com/css2?family=Josefin+Sans:wght@400;600&display=swap">
<style>
  :root {
    --page: #ffffff;
    --card: #ffffff;
    --card-shadow: rgba(0, 0, 0, 0.28);
    --label-grey: #56626b;
    --label-navy: #2f5f79;
    --rule: #7d878e;
    --cashflow: #33617b;
    --wealth: #1aa5b7;
    --on-dark: #ffffff;
  }
  html, body {
    margin: 0;
    padding: 0;
    width: 1200px;
    height: 848px;
    overflow: hidden;
    background: var(--page);
  }
  .canvas {
    display: block;
    width: 1200px;
    height: 848px;
    font-family: "Josefin Sans", "Century Gothic", sans-serif;
  }
  .card { fill: var(--card); }
  .rule {
    stroke: var(--rule);
    stroke-width: 2.2;
    stroke-dasharray: 1.5 4.5;
    stroke-linecap: round;
    fill: none;
  }
  .axis-label {
    fill: var(--label-grey);
    font-size: 28px;
    font-weight: 600;
    letter-spacing: 3px;
  }
  .field-label {
    fill: var(--label-navy);
    font-size: 21px;
    font-weight: 600;
    letter-spacing: 2px;
  }
  .cashflow-badge { fill: var(--cashflow); }
  .wealth-badge { fill: var(--wealth); }
  .badge-label {
    fill: var(--on-dark);
    font-size: 25px;
    font-weight: 600;
    letter-spacing: 2px;
  }
</style>
</head>
<body>
<svg class="canvas" viewBox="0 0 1200 848" xmlns="http://www.w3.org/2000/svg" role="img" aria-label="One page financial planning canvas">
  <defs>
    <filter id="card-shadow" x="-10%" y="-10%" width="125%" height="130%">
      <feDropShadow dx="8" dy="10" stdDeviation="9" flood-color="#000" flood-opacity="0.28"/>
    </filter>
  </defs>

  <rect class="card" x="54" y="99" width="1083" height="663" rx="17" filter="url(#card-shadow)"/>

  <!-- grid rules -->
  <g class="grid">
    <line class="rule" x1="268" y1="177" x2="268" y2="650"/>
    <line class="rule" x1="576" y1="177" x2="576" y2="358"/>
    <line class="rule" x1="576" y1="474" x2="576" y2="586"/>
    <line class="rule" x1="884" y1="177" x2="884" y2="650"/>
    <line class="rule" x1="280" y1="416" x2="452" y2="416"/>
    <line class="rule" x1="702" y1="412" x2="882" y2="412"/>
    <line class="rule" x1="897" y1="339" x2="1094" y2="339"/>
    <line class="rule" x1="897" y1="515" x2="1094" y2="515"/>
    <line class="rule" x1="113" y1="651" x2="1094" y2="651"/>
  </g>

  <!-- axis labels -->
  <text class="axis-label" x="110" y="193">GOALS</text>
  <text class="axis-label" x="110" y="695">TIME</text>

  <!-- field labels -->
  <text class="field-label" x="282" y="193">INCOME</text>
  <text class="field-label" x="282" y="451">ASSETS</text>
  <text class="field-label" x="868" y="193" text-anchor="end">EXPENSES</text>
  <text class="field-label" x="866" y="448" text-anchor="end">DEBT</text>
  <text class="field-label" x="897" y="193">FEARS</text>
  <text class="field-label" x="899" y="375">FRUSTRATIONS</text>
  <text class="field-label" x="897" y="551">PARTNERS</text>

  <!-- centre badges -->
  <ellipse class="cashflow-badge" cx="576" cy="412" rx="116" ry="44"/>
  <text class="badge-label" x="576" y="405" text-anchor="middle">CASH</text>
  <text class="badge-label" x="576" y="434" text-anchor="middle">FLOW</text>

  <path class="wealth-badge" d="M460 652 A116 63 0 0 1 692 652 Z"/>
  <text class="badge-label" x="576" y="636" text-anchor="middle">WEALTH</text>
</svg>
</body>
</html>
```